Wordpress Web Design For Midlife Lane.com

We're looking to update the design for www.midlifelane.example. The website provides news and views for people aged 50 plus.

We want to use Wordpress as the content management tool and incorporate postwren to manage subscribers to our monthly newsletter.

In terms of design, we're looking for something simple and straightforward, we quite like the elder hub site, so something like that would be good. http://www.elderhub.example.org
Updates

Project Deadline Extended
Reason: Dear All, Due to the Xmas break in the UK I've decided to extend the deadline by 7 days. Thanks for all your submissions, we will be making a decision shortly. Please note, as per the original brief, we are only interested in fully coded sites uploaded to our hosting provider. Please withdraw your design if you are not able to offer this complete solution. Thanks and good wishes to all!

Requirements
Must have
• Fully working wordpress templates that allow us to easily manage the website content. Easy for readers to use, navigate and read the content.
• Ideally a'turnkey' solution - the website built and ready for us to use wordpress to populate with content.

```html
<!DOCTYPE html>
<html lang="en">
<head>
<meta charset="utf-8">
<title>Midlife Lane.com – News and views for the over 50s</title>
<link rel="stylesheet" href="https://fonts.googleapis.com/css2?family=Montserrat:wght@400;600;700&family=Open+Sans:wght@400;600;700&family=Crimson+Text:wght@400;600;700&display=swap">
<style>
:root{
  --green:#7bb31f;
  --green-dark:#5f9813;
  --green-deep:#4f830d;
  --green-light:#9ccd3b;
  --ink:#3c3c3c;
  --muted:#6b6b6b;
  --line:#dcdcdc;
  --page:#f4f4f4;
  --white:#ffffff;
  --navy:#2b2f6b;
  --magenta:#b0166d;
  --sky:#1b8fd0;
}
*{box-sizing:border-box;margin:0;padding:0}
html,body{width:1200px;height:2210px;overflow:hidden}
body{background:var(--page);font-family:"Open Sans",Arial,sans-serif;color:var(--ink);position:relative}
.topbar{position:absolute;left:0;top:0;width:1200px;height:4px;background:var(--green)}
.header{position:absolute;left:0;top:4px;width:1200px;height:166px;background:var(--white)}
.brand{position:absolute;left:146px;top:26px;width:220px;display:flex;align-items:center;gap:12px}
.brand-dot{width:44px;height:44px;border-radius:50%;background:var(--green);flex:none}
.brand-name{font-family:"Montserrat",sans-serif;font-weight:700;font-size:24px;color:var(--green-dark);line-height:1.1}
.top-banner{position:absolute;left:378px;top:18px;width:681px;height:84px;background:linear-gradient(90deg,#3a3f8c,#262a6e);display:flex;align-items:center}
.top-banner .banner-art{width:120px;height:76px;margin-left:6px;background:linear-gradient(135deg,#e9b93a,#d3463d 60%,#6aa84f)}
.top-banner .banner-copy{flex:1;text-align:center;color:var(--white);font-family:"Montserrat",sans-serif}
.top-banner .banner-copy strong{display:block;font-size:30px;font-weight:700;line-height:1.1}
.top-banner .banner-copy span{font-size:19px}
.top-banner .banner-badge{width:160px;height:70px;margin-right:8px;background:var(--white);display:flex;align-items:center;gap:8px;padding:0 8px}
.top-banner .badge-square{width:30px;height:30px;background:#c2272d;flex:none}
.top-banner .badge-name{font-family:"Montserrat",sans-serif;font-size:13px;font-weight:700;color:var(--navy);line-height:1.1}
.nav{position:absolute;left:141px;top:122px;width:918px;height:46px;display:flex;border:1px solid var(--line);border-bottom:none;background:var(--white)}
.nav a{flex:auto;display:flex;align-items:center;justify-content:center;font-size:16px;color:#333;text-decoration:none;border-right:1px solid var(--line);font-family:"Open Sans",sans-serif}
.nav a:last-child{border-right:none}
.nav a.current{color:var(--green);border-top:3px solid var(--green)}
.nav-rule{position:absolute;left:0;top:168px;width:1200px;height:1px;background:var(--line)}

.slider{position:absolute;left:141px;top:181px;width:610px;height:252px;background:linear-gradient(120deg,#cfd6dc,#eef0ee 50%,#c9b8a6);overflow:hidden}
.slider .caption{position:absolute;left:0;bottom:0;width:100%;height:76px;background:rgba(255,255,255,.85);font-family:"Crimson Text",serif;font-size:22px;line-height:1.2;color:#222;padding:12px 48px}
.slider .arrow{position:absolute;top:124px;width:24px;height:28px;background:#4b4b4b;display:flex;align-items:center;justify-content:center}
.slider .arrow.prev{left:0}.slider .arrow.next{right:0}

.section-title{position:absolute;left:141px;top:458px;font-family:"Crimson Text",serif;font-size:22px;font-weight:600;color:#444;letter-spacing:.5px}
.section-rule{position:absolute;left:141px;top:490px;width:610px;border-top:1px dashed #c8c8c8}

.post{position:absolute;width:282px}
.post h3{font-family:"Montserrat",sans-serif;font-size:13px;font-weight:700;color:var(--green);text-transform:uppercase;line-height:1.5;height:50px;overflow:hidden}
.post .thumb{margin-top:3px;width:282px;height:164px;border:1px solid var(--line)}
.post p{margin-top:16px;font-size:13.5px;line-height:1.55;color:#444;height:62px;overflow:hidden}
.post .more{display:inline-block;margin-top:12px;padding:5px 10px;background:#e4e4e4;font-size:11px;color:#666;text-transform:uppercase;letter-spacing:.5px}
.older{position:absolute;left:403px;top:1986px;font-size:11px;font-weight:700;color:var(--green);text-transform:uppercase;letter-spacing:.5px}

.sidebar{position:absolute;left:778px;top:181px;width:281px}
.search{position:absolute;left:0;top:2px;width:281px;height:40px;border-radius:20px;background:var(--white);border:1px solid var(--line);display:flex;align-items:center;padding:0 8px 0 16px;font-size:12px;color:#999;justify-content:space-between}
.search .go{width:22px;height:22px;border-radius:50%;background:var(--green)}
.widget{position:absolute;left:0;width:281px;background:var(--white);border:1px solid var(--line)}
.widget-head{height:40px;background:linear-gradient(var(--green-light),var(--green-dark));color:var(--white);font-family:"Crimson Text",serif;font-weight:700;font-size:21px;padding:6px 8px;letter-spacing:.5px}
.field{margin:10px 8px 0;height:32px;border:1px solid var(--line);border-radius:3px;font-size:12px;color:#777;padding:7px 10px}
.login-opts{margin:12px 8px 0;font-size:11px;color:#555;display:flex;gap:14px;align-items:center}
.box{display:inline-block;width:11px;height:11px;border:1px solid #999;margin-right:4px;vertical-align:-1px}
.btn{display:inline-block;margin:10px 8px 0;padding:5px 12px;background:linear-gradient(var(--green-light),var(--green-deep));color:var(--white);font-family:"Montserrat",sans-serif;font-weight:700;font-size:15px;letter-spacing:.5px}
.register{margin:10px 8px;font-size:11px;color:#333;display:flex;align-items:center;gap:6px}
.newsletter-title{display:flex;align-items:center;gap:10px;margin:18px 8px 0;font-family:"Crimson Text",serif;font-weight:700;font-size:26px;color:#333}
.newsletter p{margin:12px 8px 0;font-size:13px;line-height:1.5;color:#555}
.promo-art{top:659px;height:232px;background:linear-gradient(150deg,#e5f0b0,#bfe06b 60%,#8fc43a);position:absolute;left:0;width:281px}
.promo-art .cta{position:absolute;left:86px;bottom:10px;width:110px;height:26px;background:#4f7f1a;color:var(--white);font-size:11px;display:flex;align-items:center;justify-content:center}
.ad{top:917px;height:555px;background:var(--white);border:1px solid var(--line);padding:8px;font-family:"Montserrat",sans-serif;position:absolute;left:0;width:281px;overflow:hidden}
.ad .ad-brand{display:flex;align-items:center;gap:6px;font-size:13px;font-weight:700;color:var(--navy);width:108px;line-height:1.1}
.ad .ad-square{width:20px;height:20px;background:var(--magenta);flex:none}
.ad .ad-head{position:absolute;left:120px;top:20px;width:156px;font-size:21px;line-height:1.2;color:var(--navy)}
.ad .ad-head em{font-style:normal;color:var(--sky)}
.ad .ad-ticks{position:absolute;left:136px;top:104px;display:flex;gap:14px}
.ad .ad-boxes{position:absolute;left:150px;top:142px;font-size:21px;color:var(--navy)}
.ad .ad-side{position:absolute;left:8px;top:100px;width:106px;font-size:15px;line-height:1.2;color:var(--magenta)}
.ad .ad-side b{color:var(--sky)}
.ad .ad-guarantee{position:absolute;left:8px;top:245px;width:265px;font-size:18px;font-weight:600;color:var(--magenta);text-align:center}
.ad .ad-guarantee span{display:block;color:var(--navy);font-weight:400;font-size:16px;margin-top:4px}
.ad .ad-photo{position:absolute;left:0;top:330px;width:120px;height:225px;background:linear-gradient(160deg,#d6e6ef,#b8d3df)}
.ad .ad-save{position:absolute;left:124px;top:340px;width:150px;font-size:21px;line-height:1.2;color:var(--sky);text-align:center}
.ad .ad-save small{display:block;font-size:13px;color:var(--navy);margin-top:8px;font-weight:700}
.ad .ad-cta{position:absolute;right:0;bottom:0;width:160px;height:26px;background:var(--sky);color:var(--white);font-size:12px;display:flex;align-items:center;justify-content:center}
.social-box{top:1499px;height:309px;position:absolute;left:0;width:281px;background:var(--white);border:1px solid #bcc3d2}
.social-box .sb-head{font-size:11px;font-weight:700;color:#333;padding:4px 6px;background:#eceef3;border-bottom:1px solid #ccc}
.social-box .sb-page{display:flex;gap:8px;padding:8px 10px;align-items:center}
.social-box .sb-dot{width:40px;height:40px;border-radius:50%;background:var(--green)}
.social-box .sb-page b{font-size:12px;color:#3b5998;display:block}
.social-box .sb-like{display:inline-block;margin-top:4px;border:1px solid #ccc;background:#f2f2f2;font-size:10px;padding:1px 6px}
.social-box .sb-count{font-size:10px;color:#555;padding:0 10px}
.faces{display:grid;grid-template-columns:repeat(6,36px);gap:9px 6px;padding:8px 10px}
.faces i{display:block;width:36px;height:36px;background:linear-gradient(#b8a48e,#6a5a4a)}
.social-box .sb-foot{position:absolute;bottom:0;left:0;right:0;border-top:1px solid #ddd;font-size:9px;color:#555;padding:6px 10px}

.footer{position:absolute;left:0;top:2073px;width:1200px;height:137px;background:linear-gradient(var(--green),var(--green-dark))}
.footer-links{position:absolute;left:0;top:22px;width:1200px;text-align:center;font-size:13px;color:var(--white)}
.footer-links a{color:var(--white);text-decoration:none}
.footer-links .sep{margin:0 7px}
.footer-rule{position:absolute;left:141px;top:56px;width:918px;border-top:1px solid rgba(255,255,255,.35)}
.copyright{position:absolute;left:141px;top:86px;font-size:11px;color:#e8f4d4}
.social-icons{position:absolute;right:141px;top:76px;display:flex;gap:10px}
.social-icons span{width:34px;height:34px;border-radius:50%;background:var(--white)}
</style>
</head>
<body>
<div class="topbar"></div>
<header class="header">
  <div class="brand"><span class="brand-dot"></span><span class="brand-name">Midlife<br>Lane.com</span></div>
  <div class="top-banner">
    <div class="banner-art" role="img" aria-label="Collage of everyday life icons for a life plan"></div>
    <div class="banner-copy"><strong>Over 50’s Life Plan</strong><span>Life cover from just 33p a day</span></div>
    <div class="banner-badge"><span class="badge-square"></span><span class="badge-name">Harbourside Mutual</span></div>
  </div>
  <nav class="nav">
    <a class="current">Home</a><a>About</a><a>Travel</a><a>Health</a><a>Hobbies</a><a>Lifestyle</a><a>Insurance</a><a>Legal</a><a>Competitions</a><a>Survey</a><a>Contact</a>
  </nav>
</header>
<div class="nav-rule"></div>

<section class="slider" role="img" aria-label="Photo of a smiling older couple reading a newspaper at breakfast">
  <div class="arrow prev"><svg width="10" height="12"><path d="M8 1 2 6l6 5z" fill="#fff"/></svg></div>
  <div class="arrow next"><svg width="10" height="12"><path d="M2 1l6 5-6 5z" fill="#fff"/></svg></div>
  <div class="caption">The purpose of Midlife Lane.com has always been to offer a dedicated service to the over 50s and their lifestyles.</div>
</section>

<h2 class="section-title">NEWS AND UPDATES</h2>
<div class="section-rule"></div>

<article class="post" style="left:141px;top:521px">
  <h3>Protect your pets from<br>hazards this Christmas</h3>
  <div class="thumb" role="img" aria-label="Puppy in a Santa hat beside a red gift box" style="background:linear-gradient(140deg,#f3f3f3,#d9c2a4 55%,#c8322c)"></div>
  <p>Vets are urging pet owners to watch out for potential hazards around their home to avoid an emergency visit to the surgery</p>
  <span class="more">Read more</span>
</article>
<article class="post" style="left:469px;top:521px">
  <h3>How hobbies help make<br>you happy</h3>
  <div class="thumb" role="img" aria-label="Older couple cycling outdoors by a lake" style="background:linear-gradient(#bcd8ef,#8fb4d8 45%,#7aa05a)"></div>
  <p>Keeping connected and active is an essential element of well being for people of all ages, but it can be harder to achieve</p>
  <span class="more">Read more</span>
</article>

<article class="post" style="left:141px;top:888px">
  <h3>Top ten tips for keeping homes<br>warm and energy bills down</h3>
  <div class="thumb" role="img" aria-label="House-shaped energy efficiency rating chart" style="background:linear-gradient(90deg,#f5f5f5,#e2e2e2 40%,#9cc84a 60%,#e6a63a 80%,#d24a33)"></div>
  <p>Four of the big six energy companies have hiked up prices before the seasonal surge in demand, and a survey for elder hub found</p>
  <span class="more">Read more</span>
</article>
<article class="post" style="left:469px;top:888px">
  <h3>Red meat, a whole body<br>treat</h3>
  <div class="thumb" role="img" aria-label="Knife standing beside a stack of raw red meat" style="background:linear-gradient(#ededed,#d9d9d9 40%,#b8262a)"></div>
  <p>Did you know that protein aids muscle mass and improves stability? Or that the average 50+ male needs 53.3 grams of</p>
  <span class="more">Read more</span>
</article>

<article class="post" style="left:141px;top:1255px">
  <h3>Clara Whitby interior design<br>masterclass</h3>
  <div class="thumb" role="img" aria-label="Bright modern interior corridor" style="background:linear-gradient(120deg,#dfe4e8,#f6f6f6 50%,#e6e0a8)"></div>
  <p>Watch our video for personal tips from Britain's 'interior designer of the moment' Clara Whitby as she takes you through a</p>
  <span class="more">Read more</span>
</article>
<article class="post" style="left:469px;top:1255px">
  <h3>How to spot the warning signs<br>of bowel cancer</h3>
  <div class="thumb" role="img" aria-label="Anatomical illustration of the digestive system" style="background:linear-gradient(#cfe3ef,#e9b7a6 50%,#c95a4c)"></div>
  <p>Log on to our live web TV show where Martin Hale, chief executive of the charity Bowel Health Trust gives up to</p>
  <span class="more">Read more</span>
</article>

<article class="post" style="left:141px;top:1622px">
  <h3>Life starts after<br>60 years</h3>
  <div class="thumb" role="img" aria-label="Older couple toasting with red wine" style="background:linear-gradient(130deg,#d8d0c4,#b58f72 55%,#6d2a24)"></div>
  <p>People aged 60+ are pursuing their dream businesses or jobs. More than a quarter do it to achieve a life goal, while nearly one in</p>
  <span class="more">Read more</span>
</article>
<article class="post" style="left:469px;top:1622px">
  <h3>Lunara therapy massage<br>candle</h3>
  <div class="thumb" role="img" aria-label="White massage candle in a glass jar" style="background:radial-gradient(circle at 50% 55%,#ffffff,#e6e6e6 45%,#c9c9c9)"></div>
  <p>The leaves are turning, summer seems like a year ago and you've cranked the central heating up - it's official, winter is definitely</p>
  <span class="more">Read more</span>
</article>

<div class="older">+ Older posts</div>

<aside class="sidebar">
  <div class="search">Search<span class="go"></span></div>
  <div class="widget" style="top:69px;height:258px">
    <div class="widget-head">LOGIN</div>
    <div class="field">Username</div>
    <div class="field">Password</div>
    <div class="login-opts"><span><i class="box"></i>Remember Me</span><span>Forgot Your Password</span></div>
    <span class="btn">SUBMIT</span>
    <div class="register"><svg width="10" height="9"><path d="M1 5l3 3 5-7" stroke="#333" stroke-width="1.6" fill="none"/></svg>Register here</div>
  </div>
  <div class="widget newsletter" style="top:345px;height:287px">
    <div class="widget-head">KEEP UP TO DATE</div>
    <div class="newsletter-title"><svg width="40" height="34"><path d="M2 14 20 2l18 12v18H2z" fill="#f2f2f2" stroke="#999"/><path d="M2 14l18 11 18-11" fill="none" stroke="#999"/></svg>Newsletter!</div>
    <p>Sign up for our fortnightly newsletter to stay on top of the latest from Midlife Lane.com.</p>
    <div class="field">Enter your email_id</div>
    <span class="btn">SUBMIT</span>
  </div>
  <div class="promo-art" role="img" aria-label="Magazines fanned out promoting a £2,500 Harrow &amp; Finch vouchers prize draw"><span class="cta">Find out more</span></div>
  <div class="ad">
    <div class="ad-brand"><span class="ad-square"></span>Kestrel Mutual Assurance</div>
    <div class="ad-head">over <em>50s life</em><br>cover that<br>ticks more</div>
    <div class="ad-ticks">
      <svg width="26" height="26"><rect x="1" y="1" width="24" height="24" fill="none" stroke="#2b2f6b" stroke-width="2"/><path d="M5 13l6 6 12-16" stroke="#b0166d" stroke-width="3" fill="none"/></svg>
      <svg width="26" height="26"><rect x="1" y="1" width="24" height="24" fill="none" stroke="#2b2f6b" stroke-width="2"/><path d="M5 13l6 6 12-16" stroke="#b0166d" stroke-width="3" fill="none"/></svg>
    </div>
    <div class="ad-boxes">boxes.</div>
    <div class="ad-side"><b>flexibility</b> to claim for serious or terminal illness</div>
    <div class="ad-guarantee">GAURANTEE ACCEPTANCE<span>WITHOUT A MEDICAL.</span></div>
    <div class="ad-photo" role="img" aria-label="Older couple relaxing outdoors"></div>
    <div class="ad-save">Save 5% on premium when you apply online.<small>SIMPLY TO APPLY.</small></div>
    <div class="ad-cta">Get a quote today</div>
  </div>
  <div class="social-box">
    <div class="sb-head">Find us on Friendbook</div>
    <div class="sb-page"><span class="sb-dot"></span><div><b>midlifelane</b><span class="sb-like">Like</span></div></div>
    <div class="sb-count">1,933 people like Midlife Lane.com</div>
    <div class="faces" role="img" aria-label="Grid of follower profile pictures">
      <i></i><i></i><i></i><i></i><i></i><i></i><i></i><i></i><i></i><i></i><i></i><i></i><i></i><i></i><i></i><i></i><i></i><i></i>
    </div>
    <div class="sb-foot">Friendbook social plugin</div>
  </div>
</aside>

<footer class="footer">
  <div class="footer-links"><a>Home</a><span class="sep">/</span><a>About Midlife Lane.com</a><span class="sep">/</span><a>Advertise</a><span class="sep">/</span><a>Privacy Policy</a><span class="sep">/</span><a>Useful Links</a><span class="sep">/</span><a>Privacy Policy</a><span class="sep">/</span><a>Terms and Conditions</a><span class="sep">/</span><a>Contact us</a></div>
  <div class="footer-rule"></div>
  <div class="copyright">© 2013 midlifelane.example. All rights reserved.</div>
  <div class="social-icons"><span title="Friendbook"></span><span title="Chatter"></span><span title="ClipTube"></span></div>
</footer>
</body>
</html>
```